Ironvale Shift Services

We are a underground coal mining labour hire company, needing a website that links into our online payroll (www.wagetrakker.com.au) and also need to have job applications page that is a preform with drop down menu,s with answers or check boxes. We would also need a 3 tier administration access for access to different files.
We are looking for an ongoing relationship with future app integration

Reason: There are a few more designs to come and I'm out at the mine for another week

Industry/Entity Type

Coal Mining

```html
<!DOCTYPE html>
<html lang="en">
<head>
<meta charset="utf-8">
<title>Ironvale Shift Services – Application Form</title>
<link rel="stylesheet" href="https://fonts.googleapis.com/css2?family=Arimo:wght@400;700&display=swap">
<style>
  :root {
    --bg: #000000;
    --panel: #3d3d3d;
    --orange: #f5832a;
    --text: #a6a6a6;
    --nav: #9a9a9a;
    --rule: #4a4a4a;
    --white: #ffffff;
    --muted: #555555;
  }
  * { box-sizing: border-box; margin: 0; padding: 0; }
  html, body { width: 1200px; height: 1042px; overflow: hidden; background: var(--bg); }
  body { position: relative; font-family: "Arimo", Arial, sans-serif; color: var(--text); }

  .brand-mark { position: absolute; left: 48px; top: 0; width: 103px; height: 147px; background: #151515; }
  .brand-name { position: absolute; left: 177px; top: 63px; font-size: 22px; font-weight: 400; color: var(--white); letter-spacing: .5px; }

  .utility { position: absolute; top: 16px; right: 28px; display: flex; align-items: center; gap: 14px; }
  .utility a { color: var(--orange); text-decoration: none; font-size: 15px; }

  .rule { position: absolute; left: 64px; width: 1069px; height: 1px; background: var(--rule); }
  .rule.top { top: 158px; }
  .rule.bottom { top: 236px; }

  .main-nav { position: absolute; top: 188px; left: 0; width: 1133px; }
  .main-nav a { position: absolute; font-size: 16px; font-weight: 700; color: var(--nav); text-decoration: none; white-space: nowrap; }

  .page-title { position: absolute; left: 72px; top: 280px; font-size: 37px; font-weight: 700; color: var(--orange); }
  .banner-art { position: absolute; left: 718px; top: 237px; width: 416px; height: 143px;
    background: linear-gradient(110deg, #000 0%, #1e1e1e 25%, #e57a2a 55%, #f3a561 70%, #1a1a1a 100%); }

  .application { position: absolute; left: 64px; top: 380px; width: 1070px; height: 516px; border: 1px solid var(--rule); }
  .question { position: absolute; left: 0; width: 1069px; display: flex; }
  .question .label { width: 703px; padding-left: 32px; font-size: 18px; color: var(--text); }
  .question .answer { flex: 1; position: relative; }
  .q-generics { top: 0; height: 73px; }
  .q-generics .label { background: var(--bg); line-height: 73px; }
  .q-generics .answer { background: var(--panel); }
  .q-medical { top: 73px; height: 73px; }
  .q-medical .label { background: var(--panel); line-height: 73px; }
  .q-medical .answer { background: var(--bg); }
  .q-mine { top: 146px; height: 369px; }
  .q-mine .label { background: var(--bg); padding-top: 22px; }
  .q-mine .answer { background: var(--panel); }

  .choice { position: absolute; font-size: 18px; color: var(--text); }
  .radio { position: absolute; width: 15px; height: 15px; border: 1.5px solid #cfcfcf; border-radius: 50%; }
  .radio.on::after { content: ""; position: absolute; left: 3.5px; top: 3.5px; width: 5px; height: 5px; border-radius: 50%; background: #cfcfcf; }
  .check { position: absolute; left: 293px; width: 17px; height: 17px; border: 1.5px solid #bdbdbd; }

  .submit { position: absolute; left: 767px; top: 897px; width: 367px; height: 85px; background: var(--orange);
    color: var(--white); font-size: 24px; font-weight: 700; text-align: center; line-height: 85px; border: 0; font-family: inherit; }

  .copyright { position: absolute; top: 1020px; left: 0; width: 1092px; text-align: center; font-size: 12px; color: var(--muted); }
</style>
</head>
<body>
  <header>
    <div class="brand-mark"></div>
    <div class="brand-name">Ironvale Shift Services</div>
    <div class="utility">
      <svg width="22" height="22" viewBox="0 0 22 22" aria-label="Search"><circle cx="9" cy="9" r="7" fill="none" stroke="#f5832a" stroke-width="1.6"/><line x1="14" y1="14" x2="20" y2="20" stroke="#f5832a" stroke-width="1.6"/></svg>
      <a href="#">LOGIN</a>
    </div>
    <div class="rule top"></div>
    <nav class="main-nav">
      <a href="#" style="left:534px">ABOUT</a>
      <a href="#" style="left:637px">DOWNLOAD DOCUMENTS</a>
      <a href="#" style="left:882px">PAY PORTAL</a>
      <a href="#" style="left:1030px">CONTACT US</a>
    </nav>
    <div class="rule bottom"></div>
  </header>

  <h1 class="page-title">APPLICATION FORM</h1>
  <div class="banner-art" role="img" aria-label="Illustration of a mine worker in a hard hat with a pick"></div>

  <form class="application">
    <div class="question q-generics">
      <div class="label">DO YOU HAVE CURRENT COAL BOARD GENERICS ?</div>
      <div class="answer">
        <span class="choice" style="left:74px;top:25px">YES</span><span class="radio on" style="left:137px;top:29px"></span>
        <span class="choice" style="left:232px;top:25px">NO</span><span class="radio" style="left:287px;top:29px"></span>
      </div>
    </div>
    <div class="question q-medical">
      <div class="label">DO YOU HAVE A CURRENT&nbsp; COAL BOARD MEDICAL ?</div>
      <div class="answer">
        <span class="choice" style="left:74px;top:17px">YES</span><span class="radio on" style="left:137px;top:21px"></span>
        <span class="choice" style="left:232px;top:17px">NO</span><span class="radio" style="left:287px;top:21px"></span>
      </div>
    </div>
    <div class="question q-mine">
      <div class="label">WHAT MINE ARE YOU CURRENTLY INDUCTED AT ?</div>
      <div class="answer">
        <span class="choice" style="left:71px;top:30px">ASHCOMBE</span><span class="check" style="top:31px"></span>
        <span class="choice" style="left:71px;top:89px">DURALEE</span><span class="check" style="top:89px"></span>
        <span class="choice" style="left:70px;top:152px">BRACKENWOLD</span><span class="check" style="top:153px"></span>
        <span class="choice" style="left:68px;top:211px">CALLOWAY CREEK</span><span class="check" style="top:211px"></span>
        <span class="choice" style="left:69px;top:269px">ETC.</span>
      </div>
    </div>
  </form>
  <button class="submit" type="submit">SUBMIT</button>

  <footer class="copyright">Copyright : ISS. 2014</footer>
</body>
</html>
```